macro advisory firm intro powerpoint

I have the bones of an introductory deck for a new firm. Need to make it much more professionally designed. Want it to also be customizable when received so I can adjust wording, etc. use colors similar to typical finance firm. high end fonts, etc.

```html
<!DOCTYPE html>
<html lang="en">
<head>
<meta charset="utf-8">
<title>Ardent Ridge Macro Advisory – Introduction Deck</title>
<link href="https://fonts.googleapis.com/css2?family=Merriweather:wght@700;900&family=Lato:wght@400;700&display=swap" rel="stylesheet">
<style>
:root{
  --navy:#12213a;
  --navy-deep:#0c182c;
  --gold:#b38b45;
  --gold-light:#c9a15a;
  --ink:#1b2436;
  --body:#333a46;
  --white:#ffffff;
  --page:#ffffff;
}
*{margin:0;padding:0;box-sizing:border-box}
html,body{width:1050px;height:1200px;overflow:hidden;background:var(--page)}
body{position:relative;font-family:'Lato',sans-serif;color:var(--body)}
.slide{position:absolute;width:454px;height:255px;background:var(--white);overflow:hidden;box-shadow:0 0 3px rgba(0,0,0,.12)}
.col-a{left:41px}.col-b{left:555px}
.row-1{top:41px}.row-2{top:329px}.row-3{top:616px}.row-4{top:904px}
.abs{position:absolute}
.serif{font-family:'Merriweather',serif;font-weight:700;color:var(--ink);text-transform:uppercase;letter-spacing:.2px}
.rule{position:absolute;width:32px;height:1.5px;background:var(--gold)}
.page-no{position:absolute;right:5px;bottom:4px;font-size:5px;color:#666}
.page-no.light{color:#cfd5df}
.gold-tab{position:absolute;top:0;height:16px;background:var(--gold)}
.icon{position:absolute;width:22px;height:22px;border-radius:50%;background:var(--gold)}
.icon::after{content:"";position:absolute;inset:6px;border:1.2px solid var(--white);border-radius:50%}
.item-title{font-weight:700;font-size:9px;color:var(--ink);line-height:1.3}
.item-text{font-size:7px;line-height:1.5;color:var(--body)}
.lead{font-size:7.4px;line-height:1.5;color:var(--body)}
.photo{position:absolute}

/* title slide */
.title-slide{background:linear-gradient(135deg,#18294a 0%,var(--navy) 50%,#0f1d35 100%)}
.brand{position:absolute;left:32px;top:47px;display:flex;gap:6px}
.brand-mark{width:22px;height:22px;background:var(--gold-light);margin-top:3px}
.brand-name{font-family:'Merriweather',serif;font-weight:700;color:#efe6d4;font-size:13px;line-height:1.1}
.brand-sub{font-size:4.8px;letter-spacing:.6px;color:#e6dcc6;margin-top:4px;line-height:1.4}
.title-slide h1{position:absolute;left:32px;top:123px;font-size:20px;line-height:1.25;color:var(--white)}
.title-slide p{position:absolute;left:32px;top:187px;width:250px;font-size:7.4px;line-height:1.6;color:#e3e7ee}

/* founder */
.founder h2{left:16px;top:12px;font-size:15.5px;line-height:1.4}
.founder .entry{position:absolute;left:47px;width:226px}
.founder .item-text{font-size:6.8px}
.founder .photo{left:280px;top:0;width:158px;height:255px;background:radial-gradient(ellipse at 60% 40%,#6a5a52 0%,#2c2a2e 55%,#141416 100%)}
.founder .side-bar{position:absolute;left:438px;top:0;width:16px;height:255px;background:var(--gold)}

/* services cards */
.card{position:absolute;top:146px;width:100px;height:92px;background:var(--navy);text-align:center;padding:18px 6px 0}
.card h4{font-size:9px;font-weight:700;color:var(--gold-light);line-height:1.15;margin-bottom:6px}
.card p{font-size:6.5px;line-height:1.6;color:var(--white)}

/* benefits */
.benefit-panel{position:absolute;left:230px;top:0;width:224px;height:255px;background:var(--navy)}
.benefit{position:absolute;width:100px;text-align:center}
.benefit-icon{position:relative;display:block;width:23px;height:23px;margin:0 auto 8px;border-radius:50%;border:1px solid var(--gold)}
.benefit-icon::after{content:"";position:absolute;inset:6px;border:1px solid var(--gold);border-radius:50%}
.benefit h4{font-family:'Merriweather',serif;font-size:7.6px;color:var(--gold-light);margin-bottom:4px;font-weight:700}
.benefit p{font-size:5.6px;line-height:1.5;color:#e5e9ef}

/* strengths */
.strengths .panel{position:absolute;left:0;top:0;width:274px;height:255px;background:linear-gradient(160deg,#14243f,var(--navy-deep))}
.strengths .item-title{color:var(--gold-light);font-size:9px;margin-bottom:2px}
.strengths .item-text{color:var(--white);font-size:7.2px}

/* engagement */
.terms .panel{position:absolute;left:0;top:82px;width:454px;height:173px;background:linear-gradient(180deg,#132440,var(--navy-deep))}
.terms .item-title{color:var(--gold-light);font-size:9.5px;margin-bottom:2px}
.terms .item-text{color:var(--white);font-size:7.4px}
</style>
</head>
<body>

<!-- 01 Title -->
<section class="slide col-a row-1 title-slide">
  <div class="brand">
    <div class="brand-mark"></div>
    <div>
      <div class="brand-name">ARDENT<br>RIDGE</div>
      <div class="brand-sub">GEOPOLITICAL<br>ECONOMIC • POLICY<br>ANALYSIS</div>
    </div>
  </div>
  <h1 class="serif">Strategic Insight<br>for an Evolving World</h1>
  <div class="rule" style="left:32px;top:176px"></div>
  <p>Our mission is to deliver clarity and actionable strategies that prepare clients for tomorrow’s challenges.</p>
</section>

<!-- 05 Co-founder -->
<section class="slide col-b row-1 founder">
  <h2 class="abs serif">Co-Founder: Daniel<br>Marsh-Corvino, Ph.D, MBA</h2>
  <div class="rule" style="left:18px;top:57px"></div>
  <p class="abs item-text" style="left:18px;top:66px;width:250px;font-size:7.2px">Economic Strategist | Author | Captain U.S. Army Reserve (SME Finance &amp; Banking) | Deputy Chief of Staff, Governor Thomas Hale</p>
  <div class="icon" style="left:18px;top:104px"></div>
  <div class="entry" style="top:102px"><div class="item-title">Government &amp; Budget Leadership</div><div class="item-text">$87B+ oversight, economic competitiveness strategy for Virginia</div></div>
  <div class="icon" style="left:18px;top:140px"></div>
  <div class="entry" style="top:138px"><div class="item-title">Defense Sector Expertise</div><div class="item-text">Captain, U.S. Army Reserve – Civil Affairs, Financial Specialization</div></div>
  <div class="icon" style="left:18px;top:176px"></div>
  <div class="entry" style="top:172px"><div class="item-title">Cross-Sector Executive</div><div class="item-text">Keystone Row Holdings (Investments), Meridian Policy Advisors (Consulting)</div></div>
  <div class="icon" style="left:18px;top:214px"></div>
  <div class="entry" style="top:210px"><div class="item-title">Thought Leadership</div><div class="item-text">Author, policy lecturer, media contributor (Capital Wire, Ledger Weekly, Civic Radio)</div></div>
  <div class="photo" role="img" aria-label="Portrait of the co-founder in a suit beside a state flag"></div>
  <div class="side-bar"></div>
  <span class="page-no light">05</span>
</section>

<!-- 02 Firm overview -->
<section class="slide col-a row-2">
  <div class="abs" style="left:303px;top:0;width:151px;height:65px;background:var(--gold)"></div>
  <h2 class="abs serif" style="left:16px;top:15px;font-size:15px;line-height:1.35">Ardent Ridge Macro<br>Advisory, LLP</h2>
  <div class="rule" style="left:16px;top:56px"></div>
  <p class="abs lead" style="left:16px;top:65px;width:220px">Our goal is to provide strategic and actionable insight today, so our clients are prepared for tomorrow</p>
  <div class="icon" style="left:16px;top:101px"></div>
  <div class="abs" style="left:49px;top:98px;width:190px"><div class="item-title">Who We Serve</div><div class="item-text">C-Suite executives, Financial Institutions, Hedge Funds, Sovereign Wealth Funds, Family Offices</div></div>
  <div class="icon" style="left:16px;top:147px"></div>
  <div class="abs" style="left:49px;top:144px;width:190px"><div class="item-title">What We Do</div><div class="item-text">Decode U.S. Public Policy Trends Thru a Sophisticated Lens of Economics, Geopolitical Analysis and Deep Relationships</div></div>
  <div class="icon" style="left:16px;top:202px"></div>
  <div class="abs" style="left:49px;top:200px;width:190px"><div class="item-title">Our Team</div><div class="item-text">Former Federal and State Government Advisors who are Economists, Academics and Practitioners</div></div>
  <div class="photo" role="img" aria-label="Hands joining puzzle pieces together" style="left:255px;top:26px;width:174px;height:206px;background:linear-gradient(150deg,#3a4049,#1f2630 60%,#2a313b)"></div>
  <span class="page-no">02</span>
</section>

<!-- 06 Advisory services -->
<section class="slide col-b row-2">
  <div class="gold-tab" style="left:0;width:93px"></div>
  <h2 class="abs serif" style="left:17px;top:55px;font-size:15px">Advisory Services</h2>
  <div class="rule" style="left:17px;top:77px"></div>
  <p class="abs lead" style="left:16px;top:88px;width:140px">Flexible Models for Strategic Insight &amp; Engagement</p>
  <div class="photo" role="img" aria-label="Advisors reviewing documents across a table" style="left:231px;top:14px;width:208px;height:122px;background:linear-gradient(120deg,#c4ccd6,#4d617b 45%,#d9dde2)"></div>
  <div class="card" style="left:14px"><h4>Retainer Advisory</h4><p>Access to Senior Advisors, Regular Updates, Strategic counsel</p></div>
  <div class="card" style="left:122.5px;padding-top:17px"><h4>Project-Based Engagements</h4><p>In-depth, Bespoke Studies with Actionable Recommendations</p></div>
  <div class="card" style="left:231px;padding-top:12px"><h4>Market Entry &amp; Due Diligence</h4><p>Full Spectrum Support for Cross-Border and Regulatory Risk, Strategic Introductions</p></div>
  <div class="card" style="left:339.5px"><h4>Speakers</h4><p>Speakers for Board Meetings, Client Conferences, Curate Panels</p></div>
  <span class="page-no">06</span>
</section>

<!-- 03 Why clients seek us -->
<section class="slide col-a row-3">
  <div class="gold-tab" style="left:0;width:93px"></div>
  <h2 class="abs serif" style="left:0;width:454px;text-align:center;top:21px;font-size:15px">Why Clients Seek Us</h2>
  <div class="rule" style="left:211px;top:43px"></div>
  <p class="abs lead" style="left:0;width:454px;text-align:center;top:52px">Credibility | Access | Results</p>
  <svg class="abs" style="left:0;top:0" width="454" height="255" viewBox="0 0 454 255" aria-hidden="true">
    <g fill="none" stroke="var(--gold)" stroke-width=".8" stroke-dasharray="2.5 2">
      <path d="M212 116 C206 86 170 86 147 103"/>
      <path d="M236 116 C242 86 278 86 301 103"/>
      <path d="M212 205 C206 232 170 232 147 213"/>
      <path d="M236 205 C242 232 278 232 301 213"/>
    </g>
    <g fill="var(--navy)">
      <path d="M145 104 l3 -3 l0.5 3.5z"/><path d="M303 104 l-3 -3 l-0.5 3.5z"/>
      <path d="M145 212 l3 3 l0.5 -3.5z"/><path d="M303 212 l-3 3 l-0.5 -3.5z"/>
    </g>
  </svg>
  <div class="abs" style="left:190px;top:140px;width:66px;text-align:center">
    <div style="width:12px;height:12px;border-radius:50%;background:var(--navy);margin:0 auto 5px"></div>
    <div style="font-family:'Merriweather',serif;font-weight:700;font-size:10px;color:var(--navy);line-height:1.2">ARDENT<br>RIDGE</div>
  </div>
  <div class="icon" style="left:27px;top:109px;width:24px;height:24px"></div>
  <div class="abs" style="left:59px;top:107px"><div class="item-title">Institutional Trust</div><div class="item-text">Experience at Senior Levels in<br>Private and Public Sector</div></div>
  <div class="icon" style="left:402px;top:109px;width:24px;height:24px"></div>
  <div class="abs" style="right:63px;top:107px;text-align:right"><div class="item-title">Institutional Trust</div><div class="item-text">Experience at Senior Levels in<br>Private and Public Sector</div></div>
  <div class="icon" style="left:27px;top:166px;width:24px;height:24px"></div>
  <div class="abs" style="left:59px;top:164px"><div class="item-title">Network Advantage</div><div class="item-text">Deep Relationships with<br>Policymakers and Regulators</div></div>
  <div class="icon" style="left:402px;top:166px;width:24px;height:24px"></div>
  <div class="abs" style="right:63px;top:164px;text-align:right"><div class="item-title">Network Advantage</div><div class="item-text">Deep Relationships with<br>Policymakers and Regulators</div></div>
  <div class="abs" style="left:361px;top:239px;width:93px;height:16px;background:var(--navy)"></div>
  <span class="page-no light">03</span>
</section>

<!-- 07 Client benefits -->
<section class="slide col-b row-3">
  <h2 class="abs serif" style="left:17px;top:15px;font-size:15px">Client Benefits</h2>
  <div class="rule" style="left:17px;top:37px"></div>
  <p class="abs lead" style="left:16px;top:47px">Turning Complexity Into Competitive Advantage</p>
  <div class="photo" role="img" aria-label="Glowing blue market chart over a dark background" style="left:0;top:105px;width:230px;height:150px;background:radial-gradient(ellipse at 75% 45%,#1f5f9a 0%,#0e2a4c 45%,#07152a 100%)"></div>
  <div class="benefit-panel">
    <div class="abs" style="left:10px;top:125px;width:92px;height:.6px;background:#4a5874"></div>
    <div class="abs" style="left:121px;top:125px;width:92px;height:.6px;background:#4a5874"></div>
    <div class="abs" style="left:111px;top:17px;width:.6px;height:92px;background:#4a5874"></div>
    <div class="abs" style="left:111px;top:138px;width:.6px;height:92px;background:#4a5874"></div>
    <div class="benefit" style="left:7px;top:26px"><span class="benefit-icon"></span><h4>Risk Mitigation</h4><p>Timely policy insight reduces exposure and regulatory surprises</p></div>
    <div class="benefit" style="left:116px;top:26px"><span class="benefit-icon"></span><h4>Improved Decisions</h4><p>Data-informed strategies accelerate institutional action</p></div>
    <div class="benefit" style="left:7px;top:149px"><span class="benefit-icon"></span><h4>Access to Networks</h4><p>Connect with U.S. stakeholders and decision-makers</p></div>
    <div class="benefit" style="left:116px;top:149px"><span class="benefit-icon"></span><h4>Custom Insight</h4><p>Tailored economic and geopolitical analysis—not generic commentary</p></div>
  </div>
  <span class="page-no light">07</span>
</section>

<!-- 04 Strengths -->
<section class="slide col-a row-4 strengths">
  <div class="panel"></div>
  <div class="icon" style="left:25px;top:41px;width:24px;height:24px"></div>
  <div class="abs" style="left:58px;top:38px;width:205px"><div class="item-title">Specialized Focus</div><div class="item-text">US policy – Defense and Defense Tech, Government Relation Strategy, Manufacturing, Tax, Trade, International Relations, Macroeconomic strategy</div></div>
  <div class="icon" style="left:25px;top:114px;width:24px;height:24px"></div>
  <div class="abs" style="left:58px;top:111px;width:205px"><div class="item-title">Operational Expertise</div><div class="item-text">Multi-Billion Dollar Budgets, Public-Private Investment Design, Government Relations Implementation</div></div>
  <div class="icon" style="left:25px;top:180px;width:24px;height:24px"></div>
  <div class="abs" style="left:58px;top:177px;width:205px"><div class="item-title">Client Impact</div><div class="item-text">Actionable Guidance for C-suites and institutional investors</div></div>
  <h2 class="abs serif" style="left:305px;top:68px;font-size:14.5px;line-height:1.4">A Strategic<br>Advisory for<br>an Evolving<br>Environment</h2>
  <div class="rule" style="left:305px;top:151px"></div>
  <p class="abs lead" style="left:305px;top:160px;width:125px">Introduction – Ardent Ridge Macro Advisory</p>
  <span class="page-no">04</span>
</section>

<!-- 08 Engagement terms -->
<section class="slide col-b row-4 terms">
  <div class="gold-tab" style="left:0;width:93px"></div>
  <div class="gold-tab" style="left:361px;width:93px"></div>
  <h2 class="abs serif" style="left:0;width:454px;text-align:center;top:19px;font-size:15px">Engagement Terms</h2>
  <div class="rule" style="left:211px;top:41px"></div>
  <p class="abs lead" style="left:0;width:454px;text-align:center;top:50px">Customizable Based on Scope, Duration, and Access Needs</p>
  <div class="panel"></div>
  <div class="icon" style="left:27px;top:125px;width:24px;height:24px"></div>
  <div class="abs" style="left:61px;top:123px;width:160px"><div class="item-title">Retainer Advisory</div><div class="item-text">6–12 month terms; includes ongoing counsel and executive briefings</div></div>
  <div class="icon" style="left:260px;top:125px;width:24px;height:24px"></div>
  <div class="abs" style="left:293px;top:123px;width:150px"><div class="item-title">Market Entry Packages</div><div class="item-text">Custom timeline for cross-border due diligence and introductions</div></div>
  <div class="icon" style="left:27px;top:191px;width:24px;height:24px"></div>
  <div class="abs" style="left:61px;top:189px;width:160px"><div class="item-title">Project-Based Studies</div><div class="item-text">3–6 month scope with fixed deliverables and stakeholder engagement</div></div>
  <div class="icon" style="left:260px;top:191px;width:24px;height:24px"></div>
  <div class="abs" style="left:293px;top:189px;width:150px"><div class="item-title">Pricing Range</div><div class="item-text">From $5K/month (retainer) to $750K+ (premium engagements)</div></div>
  <span class="page-no light">08</span>
</section>

</body>
</html>
```